New Digital Marketing Company Needs Web Design

Introduction

Pixelharbour gives advice to small businesses about their websites and digital marketing strategies and builds working relationships with clients to understand their business and maximise its online presence.

Pixelharbour offers services to support its clients needs such as: website auditing & search engine optimisation (SEO), Zelvo Promoter, Friendloop advertising, newsletter development & management, online performance reporting, email setup & management, website hosting, maintenance & backup, web development, web updates & web design.

Design Specification

The site should have a clean & professional look and use the colour scheme from the logo (attached below).

The design should consist of 2 templates; The homepage & content page.

Homepage Design

The homepage should have a header with logo, contact number and email and menu. Followed underneath by a slider and then individual blocks for key services. Under the key services should be a testimonial block with 3 testimonials. Finally the footer with company details, menu links and location map.

Header Info:

Contact number: 01592 738104
Email: info@pixelharbour-example.co.uk

Menu: Home Services About Contact

Slider Design:

The slider should be full page and show an image with text.

Key Services:

The key services should have a relevant icon and brief description.

The key services are:

Digital Marketing

Website Hosting & Management

Website Health Check (SEO)

Website Updating & Development

Newsletter Management

Email Management

Note: Lorem Ipsum can be used for brief description...

Testimonials:

There should be 3 testimonials side by side and they should include a headshot image of the person giving the testimonial.

Note: Lorem Ipsum and sample images can be used for testimonials...

Footer:

The footer should have 3 sections:

Menu links:

Digital Marketing About
Zelvo Promoter Contact
Friendloop Advertising Privacy Policy
Search Engine Optimisation (SEO) Terms & Conditions
Website Hosting FAQ
Newsletter Management

Company Information:

PixelHarbour
14 Orchard Quay
Bracknell
Berskhire
KY17 3DP
Tel: 01592 738104

Friendloop icon - Chirplet icon - Careerlane icon

Location

Zelvo map

Footer Bottom:

Copyright message.

Content Design

The content design should have the common header and footer.

Each content page should have a banner for image with text description (page title).

The content page should have area for text description and area for a video display if available.

There should be a right column (possibly) for modules (latest blog, latest Friendloop feeds, testimonial)
Updates

Reason: I have had to extend the deadline as could not review while on vacation and need to feedback to some designers for content page design. Many thanks for your understanding.

Target Market(s)

Industry/Entity Type

Digital

Number of Pages Required

2 page

Requirements
Must have
• The site should have a clean & professional look and use the colour scheme from the logo (attached below).
• The design should consist of 2 templates; The homepage & content page.

```html
<!DOCTYPE html>
<html lang="en">
<head>
<meta charset="utf-8">
<title>Pixelharbour – Digital Marketing</title>
<link rel="stylesheet" href="https://fonts.googleapis.com/css2?family=PT+Sans:wght@400;700&family=PT+Sans+Narrow&display=swap">
<style>
:root{
  --plum:#5e1f4a;
  --plum-deep:#4a1639;
  --berry:#6d1a52;
  --slate:#4b4470;
  --slate-dark:#433c63;
  --navy:#2c2858;
  --ink:#3f3a5e;
  --grey-bg:#f1f1f1;
  --tab:#7a7596;
  --muted:#55506e;
  --white:#ffffff;
}
*{margin:0;padding:0;box-sizing:border-box}
html,body{width:744px;height:1200px;overflow:hidden}
body{position:relative;font-family:"PT Sans",sans-serif;background:var(--white);color:var(--navy)}

/* header */
.site-header{position:absolute;left:0;top:0;width:744px;height:54px;background:var(--white)}
.brand{position:absolute;display:flex;align-items:center;gap:7px}
.brand-dot{border-radius:50%;background:var(--berry)}
.brand-name{font-weight:400;color:var(--berry);line-height:1}
.site-header .brand{left:124px;top:16px}
.site-header .brand-dot{width:16px;height:16px}
.site-header .brand-name{font-size:22px}
.contact{position:absolute;right:124px;text-align:right}
.contact-phone{top:8px;font-size:17px;font-weight:700;color:var(--berry);display:flex;align-items:center;gap:5px}
.contact-email{top:32px;font-size:10px;font-weight:700;color:var(--ink);display:flex;align-items:center;gap:5px}

/* nav */
.main-nav{position:absolute;left:0;top:54px;width:744px;height:21px;background:var(--slate)}
.main-nav ul{list-style:none;position:absolute;left:124px;top:0;display:flex;height:21px;align-items:center}
.main-nav li{font-size:9.5px;color:var(--white);margin-right:19px}
.main-nav .home{width:35px;height:21px;background:var(--tab);display:flex;align-items:center;justify-content:center;margin-right:12px}

/* hero */
.hero{position:absolute;left:0;top:75px;width:744px;height:252px;background:radial-gradient(ellipse at 40% 40%,#7a2f62 0%,var(--plum) 45%,var(--plum-deep) 100%)}
.hero-title{position:absolute;top:70px;width:100%;text-align:center;font-size:28px;font-weight:700;color:var(--white)}
.hero-sub{position:absolute;top:110px;width:100%;text-align:center;font-family:"PT Sans Narrow",sans-serif;font-size:27px;line-height:29px;color:var(--white)}
.hero-dots{position:absolute;top:228px;left:362px;display:flex;gap:3px}
.hero-dots span{width:6px;height:6px;border-radius:50%;background:#9a7a90}
.hero-dots span:first-child{background:var(--white)}

/* intro */
.intro{position:absolute;left:0;top:327px;width:744px;height:172px}
.intro .brand{left:0;width:744px;justify-content:center;top:24px}
.intro .brand-dot{width:13px;height:13px}
.intro .brand-name{font-size:18px}
.intro p{position:absolute;left:118px;width:508px;text-align:center;font-size:9px;line-height:15px;color:var(--navy)}

/* services */
.services{position:absolute;left:0;top:499px;width:744px;height:229px;background:var(--grey-bg)}
.section-title{position:absolute;width:100%;text-align:center;font-size:18px;font-weight:700;color:var(--slate)}
.service{position:absolute;width:150px;text-align:center}
.service svg{display:block;margin:0 auto}
.service h3{margin-top:14px;font-size:9px;font-weight:700;color:var(--berry);text-transform:uppercase;white-space:nowrap}
.service p{width:128px;margin:3px auto 0;font-size:8px;line-height:12px;color:var(--muted)}
.arrow{position:absolute;top:106px}

/* testimonials */
.testimonials{position:absolute;left:0;top:728px;width:744px;height:300px;background:radial-gradient(ellipse at 50% 70%,#8a3f63 0%,#6a2855 40%,#4f1e4a 100%)}
.testimonials .section-title{top:24px;color:var(--white);font-size:19px;display:flex;justify-content:center;align-items:center;gap:6px}
.quote{position:absolute;top:70px;width:150px;text-align:center;color:var(--white)}
.headshot{width:83px;height:77px;border-radius:50%;margin:0 auto;background:radial-gradient(circle at 50% 45%,#d9cfc8 0%,#b9aaa5 55%,#8f8590 100%)}
.quote p{width:128px;margin:10px auto 0;font-size:8px;line-height:12px}
.quote cite{display:block;margin-top:12px;font-style:normal;font-weight:700;font-size:8px}
.btn{position:absolute;left:315px;top:257px;width:121px;height:25px;border:1.5px solid var(--white);border-radius:3px;color:var(--white);font-size:8px;display:flex;align-items:center;justify-content:center}

/* footer */
.site-footer{position:absolute;left:0;top:1028px;width:744px;height:172px;background:var(--slate-dark);color:var(--white)}
.site-footer h4{position:absolute;top:23px;font-size:8px;font-weight:700;text-transform:uppercase}
.link-col{position:absolute;top:40px;list-style:none;font-size:6.5px}
.link-col li{height:14.4px}
.company{position:absolute;left:341px;top:40px;font-size:6.5px;line-height:10.3px;font-style:normal}
.map{position:absolute;left:471px;top:25px;width:149px;height:93px;background:linear-gradient(135deg,#e4e2de 0%,#d6d4cf 70%,#cfe0c7 100%)}
.footer-rule{position:absolute;left:124px;top:140px;width:496px;height:1px;background:#5d5680}
.copyright{position:absolute;left:124px;top:155px;font-size:5.5px}
.social{position:absolute;top:149px;width:16px;height:16px;border-radius:50%;background:#8a859f}
</style>
</head>
<body>

<header class="site-header">
  <div class="brand"><span class="brand-dot"></span><span class="brand-name">PixelHarbour</span></div>
  <div class="contact contact-phone">
    <svg width="13" height="13" viewBox="0 0 24 24" fill="none" stroke="#8a7f9a" stroke-width="1.6"><path d="M5 3h4l2 5-3 2a12 12 0 0 0 6 6l2-3 5 2v4a2 2 0 0 1-2 2A18 18 0 0 1 3 5a2 2 0 0 1 2-2z"/></svg>
    01592 738104
  </div>
  <div class="contact contact-email">
    <svg width="13" height="10" viewBox="0 0 26 18" fill="none" stroke="#8a7f9a" stroke-width="1.6"><rect x="1" y="1" width="24" height="16"/><path d="M1 1l12 9 12-9"/></svg>
    info@pixelharbour-example.co.uk
  </div>
</header>

<nav class="main-nav">
  <ul>
    <li class="home"><svg width="12" height="11" viewBox="0 0 24 22" fill="none" stroke="#fff" stroke-width="1.8"><path d="M2 11L12 2l10 9M5 9v11h5v-6h4v6h5V9"/></svg></li>
    <li>Services</li>
    <li>About</li>
    <li>Contact</li>
  </ul>
</nav>

<section class="hero" role="img" aria-label="Blurred night city skyline in deep purple tones">
  <h1 class="hero-title">Digital Marketing Strategies</h1>
  <p class="hero-sub">Understanding their business and maximise<br>its online presence</p>
  <div class="hero-dots"><span></span><span></span><span></span></div>
</section>

<section class="intro">
  <div class="brand"><span class="brand-dot"></span><span class="brand-name">PixelHarbour</span></div>
  <p style="top:62px">Pixelharbour gives advice to small businesses about their websites and digital marketing strategies and builds working relationships with clients to understand their business and maximise its online presence.</p>
  <p style="top:107px">Pixelharbour offers services to support its clients needs such as: website auditing &amp; search engine optimisation (SEO), Zelvo Promoter, Friendloop advertising, newsletter development &amp; management, online performance reporting, email setup &amp; management, website hosting, maintenance &amp; backup, web development, web updates &amp; web design.</p>
</section>

<section class="services">
  <h2 class="section-title" style="top:19px">Key Services</h2>
  <svg class="arrow" style="left:124px" width="12" height="22" viewBox="0 0 12 22" fill="none" stroke="#4b4470" stroke-width="1.5"><path d="M11 1L1 11l10 10"/></svg>
  <svg class="arrow" style="left:608px" width="12" height="22" viewBox="0 0 12 22" fill="none" stroke="#4b4470" stroke-width="1.5"><path d="M1 1l10 10L1 21"/></svg>

  <div class="service" style="left:135px;top:62px">
    <svg width="44" height="42" viewBox="0 0 44 42" fill="none" stroke="#4b4470" stroke-width="1.4">
      <circle cx="22" cy="21" r="6"/><circle cx="22" cy="4" r="3"/><circle cx="38" cy="14" r="3"/><circle cx="36" cy="34" r="3"/><circle cx="8" cy="36" r="3"/><circle cx="5" cy="15" r="3"/>
      <path d="M22 7v8M35 15l-8 3M34 32l-8-7M10 34l8-8M8 16l9 3"/>
    </svg>
    <h3>Digital Marketing</h3>
    <p>“The Best quality Lorem ipsum Ever!! dolor sit amet, consecutor adispicing elit. Aliquam at portitior sem. Aliquam erat volupat condimentum sed!”</p>
  </div>
  <div class="service" style="left:297px;top:62px">
    <svg width="44" height="42" viewBox="0 0 44 42" fill="none" stroke="#4b4470" stroke-width="1.4">
      <path d="M10 18a8 8 0 0 1 4-13 9 9 0 0 1 16 0 8 8 0 0 1 4 13"/>
      <rect x="12" y="12" width="20" height="7"/><rect x="12" y="19" width="20" height="7"/><rect x="12" y="26" width="20" height="7"/>
      <path d="M22 33v5M14 38h16"/><circle cx="15" cy="15.5" r="1"/><circle cx="15" cy="22.5" r="1"/><circle cx="15" cy="29.5" r="1"/>
    </svg>
    <h3>Website Hosting &amp; Management</h3>
    <p>“The Best quality Lorem ipsum Ever!! dolor sit amet, consecutor adispicing elit. Aliquam at portitior sem. Aliquam erat volupat condimentum sed!”</p>
  </div>
  <div class="service" style="left:457px;top:62px">
    <svg width="44" height="42" viewBox="0 0 44 42" fill="none" stroke="#4b4470" stroke-width="1.4">
      <rect x="6" y="32" width="5" height="8"/><rect x="13" y="29" width="5" height="11"/><rect x="20" y="25" width="5" height="15"/><rect x="27" y="20" width="5" height="20"/>
      <path d="M6 30c14-2 24-10 28-24M34 6l-6 2M34 6l1 6"/><path d="M36 40V14"/>
    </svg>
    <h3>Website Health Check (SEO)</h3>
    <p>“The Best quality Lorem ipsum Ever!! dolor sit amet, consecutor adispicing elit. Aliquam at portitior sem. Aliquam erat volupat condimentum sed!”</p>
  </div>
</section>

<section class="testimonials" role="img" aria-label="Blurred warm city lights in purple and orange tones">
  <h2 class="section-title">
    <svg width="44" height="30" viewBox="0 0 44 30" fill="none" stroke="#fff" stroke-width="1.3"><ellipse cx="16" cy="11" rx="14" ry="9"/><path d="M8 18l-3 6 8-4"/><ellipse cx="28" cy="17" rx="14" ry="9" fill="#6a2855"/><path d="M36 24l3 5-8-3"/></svg>
    Testimonials
  </h2>
  <div class="quote" style="left:111px">
    <div class="headshot" role="img" aria-label="Headshot of Mira Solanki"></div>
    <p>“The Best quality Lorem ipsum Ever!! dolor sit amet, consecutor adispicing elit. Aliquam at portitior sem. Aliquam erat volupat condimentum sed!”</p>
    <cite>Mira Solanki, Sector 1, USA</cite>
  </div>
  <div class="quote" style="left:298px">
    <div class="headshot" role="img" aria-label="Headshot of Devan Pillai"></div>
    <p>“The Best quality Lorem ipsum Ever!! dolor sit amet, consecutor adispicing elit. Aliquam at portitior sem. Aliquam erat volupat condimentum sed!”</p>
    <cite>Devan Pillai, San Jose, UK</cite>
  </div>
  <div class="quote" style="left:484px">
    <div class="headshot" role="img" aria-label="Headshot of Kiran Mehta"></div>
    <p>“The Best quality Lorem ipsum Ever!! dolor sit amet, consecutor adispicing elit. Aliquam at portitior sem. Aliquam erat volupat condimentum sed!”</p>
    <cite>Kiran Mehta, Tent Bridege, UK</cite>
  </div>
  <div class="btn">READ ALL TESTIMONIALS</div>
</section>

<footer class="site-footer">
  <h4 style="left:124px">Important Links</h4>
  <ul class="link-col" style="left:124px">
    <li>Digital Marketing</li><li>About</li><li>Zelvo Promoter</li><li>Contact</li><li>Friendloop Advertising</li><li>Privacy Policy</li>
  </ul>
  <ul class="link-col" style="left:214px">
    <li>Search Engine Optimisation (SEO)</li><li>Terms &amp; Conditions</li><li>Website Hosting</li><li>FAQ</li><li>Newsletter</li><li>Management</li>
  </ul>
  <h4 style="left:341px">Company Information</h4>
  <address class="company">PixelHarbour<br>14 Orchard Quay<br>Bracknell<br>Berskhire<br>KY17 3DP<br>Tel: 01592 738104</address>
  <div class="map" role="img" aria-label="Street map showing the office location with a red pin"></div>
  <div class="footer-rule"></div>
  <p class="copyright">Copyright © 2016 pixelharbour. All rights reserved.</p>
  <span class="social" style="left:562px" role="img" aria-label="Friendloop"></span>
  <span class="social" style="left:583px" role="img" aria-label="Chirplet"></span>
  <span class="social" style="left:604px" role="img" aria-label="Careerlane"></span>
</footer>

</body>
</html>
```